Travel video blogger needs website design

I need a website designed for my new travel video blog "Roaming Sparrow". I have only just started but need a website that is fairly simple and not too busy. I have a logo which I want on it (I have attached it to this project). I also want a link to all my other social medias on the main page (vidtrekhub, Snapwell and Palnook) and my videos as well. Here is a link to my vidtrekhub page for you to look at: https://www.vidtrekhub.net/channel/QRm4tZ8pWnE2HX57YKccd31v
As I have only just started and I am still trying to find my specific niche, again I need it to be sleek and simple that I can go in and change slightly here and there. I would like these pages on the website: About Me, Videos, Social Media, Blog, Gallery, contact me. for an example I like the look of www.theroamingkinfolk.net website.

I already have the domain and I am with Harborweb with pagecraftr.org. I just want to spend my time getting better and learning about videos then trying to create a website (I am a bit of a perfectionist when I try to do something).

Target Market(s)

Young Adults (majority females) between the ages of 18 and 30 with an interest in travelling.

Industry/Entity Type

Travel Industry

Number of Pages Required

1 page

Colors

Designer to choose colors to be used in the design.

Requirements
Must have
• A like to my Snapwell, Palnook and vidtrekhub channels on the home page
• Must be a nice, simple design
• Must have my logo on the front and name "Roaming Sparrow"
Nice to have
• A nice light, bright coloured theme
Should not have
• A dark coloured theme

```html
<!DOCTYPE html>
<html lang="en">
<head>
<meta charset="utf-8">
<title>Roaming Sparrow – Travel the world with me</title>
<link href="https://fonts.googleapis.com/css2?family=Montserrat:wght@400;500;600;700&family=Open+Sans:wght@400;600&family=Kaushan+Script&display=swap" rel="stylesheet">
<style>
:root{
  --gold:#d9a86c;
  --gold-soft:#e6bf8c;
  --gold-band:#e4b57d;
  --cream:#f7eee2;
  --ink:#2b2b2b;
  --body:#666;
  --muted:#999;
  --line:#e3e3e3;
  --white:#fff;
  --night:#1c1c1c;
}
*{box-sizing:border-box;margin:0;padding:0}
html,body{width:1200px;height:5357px;overflow:hidden}
body{font-family:"Open Sans",Arial,sans-serif;color:var(--body);background:var(--white);position:relative}
a{color:inherit;text-decoration:none}
.script{font-family:"Kaushan Script",cursive}
.section-title{font-family:"Montserrat",sans-serif;font-weight:500;color:var(--gold);font-size:28px;letter-spacing:3px;text-align:center}
.section-title + .rule{display:block;width:90px;height:14px;margin:12px auto 0}

/* header + hero */
.hero{position:absolute;top:0;left:0;width:1200px;height:778px;
  background:linear-gradient(180deg,#6f8396 0%,#8fa0ad 30%,#5c6a6f 55%,#3e4548 80%,#2f3335 100%)}
.hero-photo{position:absolute;inset:0;
  background:radial-gradient(ellipse 360px 420px at 1010px 360px,#c9a88a 0%,rgba(201,168,138,.55) 45%,rgba(0,0,0,0) 75%),
             linear-gradient(180deg,rgba(255,255,255,.0) 0%,rgba(40,40,40,.25) 100%)}
.site-header{position:absolute;top:0;left:0;width:1200px;height:80px;background:rgba(0,0,0,.35);display:flex;align-items:center;padding:0 36px}
.brand{display:flex;align-items:center;gap:12px;font-family:"Montserrat",sans-serif;font-weight:600;color:var(--white);font-size:18px;letter-spacing:1px}
.brand-dot{width:58px;height:58px;border-radius:50%;background:var(--gold)}
.main-nav{margin-left:auto;display:flex;gap:6px;font-family:"Montserrat",sans-serif;font-size:14px;color:var(--white)}
.main-nav a:not(:last-child)::after{content:"|";margin-left:6px;opacity:.6}
.main-nav .active{color:var(--gold-soft)}
.header-social{margin-left:70px;display:flex;gap:10px;font-family:"Montserrat",sans-serif;font-size:11px;color:var(--white)}
.hero-copy{position:absolute;left:105px;top:400px;color:var(--white)}
.hero-copy .kicker{font-family:"Montserrat",sans-serif;font-size:20px;margin-left:80px}
.hero-copy h1{font-family:"Kaushan Script",cursive;font-weight:400;font-size:50px;margin-top:6px;letter-spacing:1px}
.btn-ghost{display:inline-block;margin:22px 0 0 80px;border:1px solid rgba(255,255,255,.8);color:var(--white);font-family:"Montserrat",sans-serif;font-size:13px;padding:10px 22px}
.slider-dots{position:absolute;top:724px;left:573px;display:flex;gap:8px}
.slider-dots span{width:10px;height:10px;border-radius:50%;background:rgba(255,255,255,.5)}
.slider-dots span:first-child{background:var(--white)}

/* gallery */
.gallery{position:absolute;top:778px;left:0;width:1200px;height:1197px;background:var(--white)}
.gallery .section-title{margin-top:106px}
.gallery-grid{position:absolute;top:204px;left:134px;display:grid;grid-template-columns:repeat(3,296px);column-gap:25px;row-gap:33px}
.place-card{height:421px;background:var(--white);box-shadow:0 2px 10px rgba(0,0,0,.12)}
.place-photo{height:196px}
.place-name{height:46px;background:#111;color:var(--white);font-family:"Montserrat",sans-serif;font-weight:600;font-size:17px;display:flex;align-items:center;padding-left:14px}
.place-tags{height:28px;background:var(--gold-soft);display:flex;font-size:11px;color:var(--white)}
.place-tags span{flex:1;padding:7px 14px}
.place-tags span+span{background:var(--gold)}
.place-text{font-size:11px;line-height:17px;padding:14px 40px 0 14px;color:var(--muted)}
.btn-small{display:inline-block;margin:18px 0 0 14px;border:1px solid var(--line);font-size:11px;padding:7px 16px;color:var(--muted)}

/* contact + about */
.contact-band{position:absolute;top:1975px;left:0;width:1200px;height:996px;
  background:linear-gradient(180deg,#fbf5ee 0%,#f6ebdd 60%,#efe0cc 100%)}
.contact-box{position:absolute;top:157px;left:132px;width:611px;height:682px;background:var(--white);padding:26px 28px}
.label-gold{font-family:"Montserrat",sans-serif;font-size:14px;color:var(--gold);letter-spacing:1px}
.contact-intro{font-size:12px;line-height:18px;margin-top:12px;color:var(--body)}
.contact-form{margin-top:22px;border:2px solid var(--gold-soft);height:500px;padding:30px 60px}
.field{display:block;font-size:12px;color:var(--body);margin-bottom:16px}
.field span{display:block;margin-bottom:4px}
.field i{display:block;width:322px;height:34px;border:1px solid #ccc;background:#fafafa}
.field.msg i{width:478px;height:96px}
.btn-send{display:inline-block;margin-top:8px;background:var(--gold);color:var(--white);font-size:12px;padding:9px 30px}
.about-card{position:absolute;top:157px;left:768px;width:303px;height:403px;background:var(--white);padding:18px 18px 0}
.about-photo{height:270px;margin-top:12px}
.about-card h3{font-family:"Montserrat",sans-serif;font-size:12px;font-weight:600;color:var(--ink);text-align:center;margin-top:14px;line-height:16px}
.about-card p{font-size:11px;line-height:15px;text-align:center;margin-top:6px}
.video-card{position:absolute;top:650px;left:768px;width:303px;height:185px}
.play{position:absolute;left:131px;top:72px;width:42px;height:42px}

/* quote banner */
.quote-band{position:absolute;top:2971px;left:0;width:1200px;height:332px;
  background:linear-gradient(180deg,#2a2d30 0%,#3a3b38 50%,#2b2a27 100%)}
.quote-band p{position:absolute;top:64px;width:1200px;text-align:center;color:var(--white);font-size:36px;line-height:52px}
.quote-social{position:absolute;top:206px;width:1200px;display:flex;justify-content:center;gap:12px}
.quote-social a{border:2px solid var(--white);border-radius:24px;color:var(--white);font-family:"Montserrat",sans-serif;font-size:12px;padding:9px 16px}

/* blog */
.blog{position:absolute;top:3303px;left:0;width:1200px;height:804px;
  background:linear-gradient(180deg,#faf3ea 0%,#f3e4d0 100%)}
.blog .section-title{margin-top:120px}
.blog-grid{position:absolute;top:239px;left:132px;display:grid;grid-template-columns:repeat(3,297px);column-gap:25px}
.post-card{height:422px;background:var(--white)}
.post-photo{height:190px;position:relative}
.post-date{position:absolute;top:12px;right:12px;background:var(--gold-soft);color:var(--white);font-family:"Montserrat",sans-serif;font-weight:600;font-size:13px;padding:6px 10px}
.post-card h3{font-family:"Montserrat",sans-serif;font-size:15px;font-weight:600;color:var(--ink);line-height:20px;padding:22px 34px 0 22px}
.post-tags{display:flex;gap:8px;padding:12px 22px 0}
.post-tags span{border:1px solid var(--line);font-size:9px;padding:3px 10px;color:var(--muted)}
.btn-read{display:inline-block;margin:22px 0 0 22px;border:1px solid var(--line);font-size:10px;font-weight:600;color:var(--ink);padding:6px 14px}

/* passion banner */
.passion{position:absolute;top:4107px;left:0;width:1200px;height:339px;
  background:linear-gradient(90deg,#4b4038 0%,#6b6b70 40%,#9aa3ad 100%)}
.passion p{position:absolute;left:520px;top:54px;color:var(--white);font-size:34px;line-height:44px;text-align:center}
.btn-pill{position:absolute;left:650px;top:170px;border:2px solid var(--white);border-radius:30px;color:var(--white);font-size:14px;padding:13px 34px}

/* map */
.map{position:absolute;top:4446px;left:0;width:1200px;height:661px;background:linear-gradient(180deg,#eef0f2 0%,#e4e7ea 100%)}
.pin{position:absolute;width:26px;height:34px}
.map-popup{position:absolute;left:482px;top:154px;width:236px;height:346px;background:var(--white);box-shadow:0 2px 10px rgba(0,0,0,.12);padding:0 0 0}
.map-popup .photo{height:160px}
.map-popup h4{font-family:"Montserrat",sans-serif;font-size:13px;font-weight:600;color:var(--ink);text-align:center;margin-top:18px}
.map-popup p{font-size:11px;line-height:16px;text-align:center;padding:8px 16px 0}

/* footer */
.site-footer{position:absolute;top:5107px;left:0;width:1200px;height:171px;background:var(--gold-band);color:var(--white)}
.footer-col{position:absolute;top:34px}
.footer-col h5{font-family:"Montserrat",sans-serif;font-size:17px;font-weight:600;letter-spacing:1px}
.footer-col p{font-size:12px;line-height:18px;margin-top:6px}
.footer-links{display:flex;gap:12px;font-size:11px;margin-top:18px}
.subscribe{display:flex;margin-top:18px}
.subscribe span{width:180px;height:34px;background:var(--white);color:#888;font-size:12px;padding:9px 10px}
.subscribe b{background:#111;font-size:12px;font-weight:600;padding:9px 20px}
.legal{position:absolute;top:5278px;left:0;width:1200px;height:79px;background:var(--night);color:#aaa;font-size:11px;text-align:center;line-height:79px}
</style>
</head>
<body>

<section class="hero">
  <div class="hero-photo" role="img" aria-label="Mountain lake at dusk with the blogger smiling on the right"></div>
  <header class="site-header">
    <a class="brand" href="#"><span class="brand-dot"></span>ROAMING SPARROW</a>
    <nav class="main-nav">
      <a class="active" href="#">Home</a><a href="#">About Me</a><a href="#">Videos</a><a href="#">Social Media</a><a href="#">Blog</a><a href="#">Gallery</a><a href="#">Contact</a>
    </nav>
    <div class="header-social"><a href="#">Palnook</a><a href="#">Snapwell</a><a href="#">Vidtrekhub</a></div>
  </header>
  <div class="hero-copy">
    <p class="kicker">Welcome to my blog</p>
    <h1>Travel the world with me</h1>
    <a class="btn-ghost" href="#">View More Details</a>
  </div>
  <div class="slider-dots"><span></span><span></span><span></span></div>
</section>

<section class="gallery">
  <h2 class="section-title">GALLERY</h2>
  <svg class="rule" viewBox="0 0 90 14"><line x1="0" y1="7" x2="36" y2="7" stroke="#d9a86c"/><circle cx="45" cy="7" r="4" fill="none" stroke="#d9a86c"/><line x1="54" y1="7" x2="90" y2="7" stroke="#d9a86c"/></svg>
  <div class="gallery-grid">
    <article class="place-card"><div class="place-photo" role="img" aria-label="Camel resting in the desert near Dubai" style="background:linear-gradient(180deg,#f0a250,#b5542c)"></div><div class="place-name">Dubai</div><div class="place-tags"><span>Desert</span><span>Skyline</span></div><p class="place-text">Golden dunes, tall towers and warm nights by the sea. A city of bright markets and calm sand.</p><a class="btn-small" href="#">Details</a></article>
    <article class="place-card"><div class="place-photo" role="img" aria-label="Buddha statues in front of city towers" style="background:linear-gradient(180deg,#4d8fd0,#8a8f86)"></div><div class="place-name">Berlin</div><div class="place-tags"><span>Culture</span><span>History</span></div><p class="place-text">Old walls, quiet parks and busy streets. A city of art, music and long evening walks.</p><a class="btn-small" href="#">Details</a></article>
    <article class="place-card"><div class="place-photo" role="img" aria-label="Domed monument silhouetted at sunset" style="background:linear-gradient(180deg,#c2417a,#f09a5a)"></div><div class="place-name">New Delhi</div><div class="place-tags"><span>Temples</span><span>Food</span></div><p class="place-text">Spice stalls, grand domes and rose sunsets. A city that fills every sense at once.</p><a class="btn-small" href="#">Details</a></article>
    <article class="place-card"><div class="place-photo" role="img" aria-label="Overwater huts on a turquoise lagoon" style="background:linear-gradient(180deg,#3aa0d8,#35c3b8)"></div><div class="place-name">Cuba</div><div class="place-tags"><span>Islands</span><span>Beach</span></div><p class="place-text">Clear water, soft sand and slow days. An island made for sun, music and rest.</p><a class="btn-small" href="#">Details</a></article>
    <article class="place-card"><div class="place-photo" role="img" aria-label="Rows of carved prayer wheels" style="background:linear-gradient(180deg,#8a8a8a,#3d3d3d)"></div><div class="place-name">Rome</div><div class="place-tags"><span>Ruins</span><span>Streets</span></div><p class="place-text">Stone lanes, old squares and fine coffee. A city where history waits at each turn.</p><a class="btn-small" href="#">Details</a></article>
    <article class="place-card"><div class="place-photo" role="img" aria-label="Boat on a misty river between mountains" style="background:linear-gradient(180deg,#c99a5e,#2f3a3a)"></div><div class="place-name">London</div><div class="place-tags"><span>Rivers</span><span>Markets</span></div><p class="place-text">Misty rivers, red buses and cosy corners. A city of parks, pubs and old bridges.</p><a class="btn-small" href="#">Details</a></article>
  </div>
</section>

<section class="contact-band">
  <div class="contact-box">
    <h2 class="label-gold">CONTACT ME</h2>
    <p class="contact-intro">Have a question about a trip, a video or working together? Send me a short note below and I will get back to you soon. I love hearing from fellow travellers and readers from every corner of the world.</p>
    <form class="contact-form">
      <label class="field"><span>Name</span><i></i></label>
      <label class="field"><span>Email</span><i></i></label>
      <label class="field"><span>Subject</span><i></i></label>
      <label class="field msg"><span>Message</span><i></i></label>
      <span class="btn-send">SEND</span>
    </form>
  </div>
  <aside class="about-card">
    <h2 class="label-gold">ABOUT ME</h2>
    <div class="about-photo" role="img" aria-label="Traveller with raised arms on a mountain top" style="background:linear-gradient(180deg,#e9b77a,#7a5a3e)"></div>
    <h3>Welcome to my family here at Roaming Sparrow!<br>My name is Maren</h3>
    <p>I am 22 and I left my desk job to travel. Follow me as I roam around the world.</p>
  </aside>
  <div class="video-card" role="img" aria-label="Video still of boats in a green tropical bay" style="background:linear-gradient(180deg,#2f6f7a,#3f8a5a)">
    <svg class="play" viewBox="0 0 42 42"><circle cx="21" cy="21" r="20" fill="rgba(0,0,0,.55)"/><path d="M16 12 L31 21 L16 30 Z" fill="#fff"/></svg>
  </div>
</section>

<section class="quote-band" role="img" aria-label="Kayak paddle over dark water">
  <p class="script">I'm the traveller, writer and person behind<br>Roaming Sparrow, a travel blog!</p>
  <div class="quote-social"><a href="#">Palnook</a><a href="#">Snapwell</a><a href="#">Vidtrekhub</a></div>
</section>

<section class="blog">
  <h2 class="section-title">BLOG POSTS</h2>
  <svg class="rule" viewBox="0 0 90 14"><line x1="0" y1="7" x2="36" y2="7" stroke="#d9a86c"/><circle cx="45" cy="7" r="4" fill="none" stroke="#d9a86c"/><line x1="54" y1="7" x2="90" y2="7" stroke="#d9a86c"/></svg>
  <div class="blog-grid">
    <article class="post-card"><div class="post-photo" role="img" aria-label="Sandstone temple under blue sky" style="background:linear-gradient(180deg,#6aa6d6,#c9803f)"><span class="post-date">15 JULY</span></div><h3>Lorem ipsum dolor sit amet, enim detracto vulputate eum ad.</h3><div class="post-tags"><span>Adventure</span><span>Culture</span></div><a class="btn-read" href="#">READ MORE</a></article>
    <article class="post-card"><div class="post-photo" role="img" aria-label="Colourful festival dancers" style="background:linear-gradient(180deg,#d94f8a,#f2b04a)"><span class="post-date">15 JULY</span></div><h3>Lorem ipsum dolor sit amet, enim detracto vulputate eum ad.</h3><div class="post-tags"><span>Festival</span><span>People</span></div><a class="btn-read" href="#">READ MORE</a></article>
    <article class="post-card"><div class="post-photo" role="img" aria-label="Camel caravan crossing desert dunes" style="background:linear-gradient(180deg,#e8a968,#a8663a)"><span class="post-date">15 JULY</span></div><h3>Lorem ipsum dolor sit amet, enim detracto vulputate eum ad.</h3><div class="post-tags"><span>Desert</span></div><a class="btn-read" href="#">READ MORE</a></article>
  </div>
</section>

<section class="passion" role="img" aria-label="Hiker sitting on a ridge above a misty valley">
  <p class="script">Travelling is my Biggest Passion<br>Your journey begins with me</p>
  <a class="btn-pill" href="#">Follow my daily updates</a>
</section>

<section class="map">
  <div role="img" aria-label="Pale world map" style="position:absolute;inset:0;background:radial-gradient(ellipse 520px 260px at 600px 330px,#dde1e5,rgba(0,0,0,0))"></div>
  <svg class="pin" style="left:196px;top:194px" viewBox="0 0 26 34"><path d="M13 33 C13 33 2 19 2 12 A11 11 0 0 1 24 12 C24 19 13 33 13 33Z" fill="#e4b57d"/><circle cx="13" cy="12" r="4" fill="#fff"/></svg>
  <svg class="pin" style="left:380px;top:260px" viewBox="0 0 26 34"><path d="M13 33 C13 33 2 19 2 12 A11 11 0 0 1 24 12 C24 19 13 33 13 33Z" fill="#e4b57d"/><circle cx="13" cy="12" r="4" fill="#fff"/></svg>
  <svg class="pin" style="left:448px;top:258px" viewBox="0 0 26 34"><path d="M13 33 C13 33 2 19 2 12 A11 11 0 0 1 24 12 C24 19 13 33 13 33Z" fill="#e4b57d"/><circle cx="13" cy="12" r="4" fill="#fff"/></svg>
  <svg class="pin" style="left:540px;top:300px" viewBox="0 0 26 34"><path d="M13 33 C13 33 2 19 2 12 A11 11 0 0 1 24 12 C24 19 13 33 13 33Z" fill="#e4b57d"/><circle cx="13" cy="12" r="4" fill="#fff"/></svg>
  <svg class="pin" style="left:360px;top:490px" viewBox="0 0 26 34"><path d="M13 33 C13 33 2 19 2 12 A11 11 0 0 1 24 12 C24 19 13 33 13 33Z" fill="#e4b57d"/><circle cx="13" cy="12" r="4" fill="#fff"/></svg>
  <svg class="pin" style="left:860px;top:130px" viewBox="0 0 26 34"><path d="M13 33 C13 33 2 19 2 12 A11 11 0 0 1 24 12 C24 19 13 33 13 33Z" fill="#e4b57d"/><circle cx="13" cy="12" r="4" fill="#fff"/></svg>
  <svg class="pin" style="left:730px;top:326px" viewBox="0 0 26 34"><path d="M13 33 C13 33 2 19 2 12 A11 11 0 0 1 24 12 C24 19 13 33 13 33Z" fill="#e4b57d"/><circle cx="13" cy="12" r="4" fill="#fff"/></svg>
  <svg class="pin" style="left:1000px;top:288px" viewBox="0 0 26 34"><path d="M13 33 C13 33 2 19 2 12 A11 11 0 0 1 24 12 C24 19 13 33 13 33Z" fill="#e4b57d"/><circle cx="13" cy="12" r="4" fill="#fff"/></svg>
  <svg class="pin" style="left:1090px;top:480px" viewBox="0 0 26 34"><path d="M13 33 C13 33 2 19 2 12 A11 11 0 0 1 24 12 C24 19 13 33 13 33Z" fill="#e4b57d"/><circle cx="13" cy="12" r="4" fill="#fff"/></svg>
  <div class="map-popup">
    <div class="photo" role="img" aria-label="Palm trees on a tropical beach" style="background:linear-gradient(180deg,#4aa7d8,#6cb36a 70%,#e9d6a6)"></div>
    <h4>5 Reasons to visit this place</h4>
    <p>White sand, warm water and kind locals. Here is why this island stole my heart on the first day.</p>
  </div>
</section>

<footer class="site-footer">
  <div class="footer-col" style="left:93px"><h5>CONTACT ME</h5><p>+1 555 010 2040<br>hello@roamingsparrow.net</p></div>
  <div class="footer-col" style="left:432px"><h5>CONNECT WITH US</h5><p>Social Media Channels</p><div class="footer-links"><a href="#">Palnook</a><a href="#">Snapwell</a><a href="#">Vidtrekhub</a></div></div>
  <div class="footer-col" style="left:764px"><h5>NEWSLETTER</h5><p>Signup for special offers</p><div class="subscribe"><span>Email</span><b>SUBSCRIBE</b></div></div>
</footer>
<div class="legal">© 2016 Roaming Sparrow All Right Reserved.</div>

</body>
</html>
```